Medical Device - Case Study Template

We need a TEMPLATE that we can reuse to write various case studies about the medical equipment solutions we provide. It will be a double sided letter sized with a modern design that conveys a feeling of expertise, innovation and highly personable service AND be consistent with the brand guide. The content will be divided into a few sections:

- Situation (200-250 words)
- Challenge (100-120 words)
- Solution (100-120 words)
- Results (100-120 words)
- Conclusion (100-120 words)

Additionally, there will need to be a call to action, inviting people to send an email for more information and a short "About Valtu" section (approx. 40 words).

For device picture placeholders, feel free to use any random small benchtop medical device.

```html
<!DOCTYPE html>
<html lang="en">
<head>
<meta charset="utf-8">
<title>Valtu – Medical Device Case Study Template</title>
<link href="https://fonts.googleapis.com/css2?family=Montserrat:wght@400;500;600;700&display=swap" rel="stylesheet">
<style>
:root{
  --navy:#0c2559;
  --heading:#13275a;
  --orange:#e07a36;
  --orange-soft:rgba(224,122,54,.92);
  --ink:#2a2f3d;
  --steel:#6f8fb4;
  --rule:#b9bcc4;
  --paper:#ffffff;
  --stage:#ffffff;
}
*{margin:0;padding:0;box-sizing:border-box}
html,body{width:1200px;height:1200px;overflow:hidden;background:var(--stage);font-family:"Montserrat",sans-serif;color:var(--ink)}
.canvas{position:relative;width:1200px;height:1200px}
.page{position:absolute;top:276px;width:506px;height:655px;background:var(--paper);overflow:hidden;box-shadow:0 1px 6px rgba(0,0,0,.12)}
.page--front{left:72px}
.page--back{left:628px}

/* brand */
.brand{position:absolute;left:26px;top:26px;display:flex;align-items:center;gap:8px}
.brand__dot{width:30px;height:30px;border-radius:50%;background:var(--orange)}
.brand__name{font-size:26px;font-weight:500;color:var(--steel);line-height:1;letter-spacing:1px}
.brand__tag{font-size:9px;font-weight:500;color:var(--steel);letter-spacing:.6px;margin-top:3px}

.pattern-area{position:absolute;left:256px;top:0;width:250px;height:87px;background:linear-gradient(90deg,rgba(255,255,255,0),rgba(170,190,220,.35))}

.hero-photo{position:absolute;left:0;top:87px;width:506px;height:188px;background:linear-gradient(110deg,#23306e 0%,#5e6fa8 30%,#c9d3e6 58%,#8f9dbf 80%,#5b6796 100%)}
.hero-band{position:absolute;left:0;top:187px;width:250px;height:88px;background:var(--orange-soft);clip-path:polygon(0 0,200px 0,250px 100%,0 100%)}
.hero-title{position:absolute;left:26px;top:206px;color:#fff;font-weight:700;line-height:1}
.hero-title__small{display:block;font-size:18.5px;letter-spacing:.3px}
.hero-title__large{display:block;font-size:26px;margin-top:3px;letter-spacing:.3px}
.hero-rule{position:absolute;left:26px;top:258px;width:70px;height:2px;background:#fff}

/* sections */
.section{position:absolute}
.section__head{display:flex;align-items:center;gap:7px;height:22px}
.section__icon{width:22px;height:22px;flex:none}
.section__title{font-size:11.5px;font-weight:700;color:var(--heading);letter-spacing:.3px}
.section__body{font-size:6.3px;line-height:7.95px;margin-top:4px;overflow:hidden}
.section__body p+p{margin-top:7px}

.col-left{left:26px;width:228px}
.col-right{left:278px;width:202px}

/* back page */
.text-block{position:absolute}
.text-block__title{font-size:11.5px;font-weight:700;color:var(--heading);letter-spacing:.3px}
.text-block__body{font-size:6.3px;line-height:7.95px;margin-top:12px;overflow:hidden}
.text-block__body p+p{margin-top:7px}

.photo{position:absolute}
.photo--monitor{left:256px;top:0;width:250px;height:196px;background:linear-gradient(135deg,#bcc5cc 0%,#e8edf1 45%,#9fb0bf 70%,#d6dde3 100%)}
.photo--clinician{left:0;top:295px;width:236px;height:298px;background:linear-gradient(160deg,#eef1f3 0%,#c5d0db 35%,#4a6ea8 65%,#2b4e9a 100%)}

/* footer */
.footer{position:absolute;left:0;right:0;bottom:0;height:53px;background:var(--navy);display:flex;align-items:center;justify-content:center;gap:11px;color:#fff;font-size:15px;font-weight:400;white-space:nowrap}
.footer-rule{position:absolute;left:0;bottom:53px;width:482px;height:3px;background:var(--rule)}
.footer-corner{position:absolute;right:0;bottom:53px}
.contact{display:flex;align-items:center;gap:6px;flex:none}
.contact svg{width:14px;height:14px;flex:none}
.contact-sep{flex:none}
</style>
</head>
<body>
<div class="canvas">

  <!-- FRONT PAGE -->
  <section class="page page--front">
    <div class="brand">
      <span class="brand__dot"></span>
      <div>
        <div class="brand__name">valtu</div>
        <div class="brand__tag">Medical Technology</div>
      </div>
    </div>
    <div class="pattern-area" role="img" aria-label="Faint molecular hexagon pattern"></div>

    <div class="hero-photo" role="img" aria-label="Clinician adjusting a medical monitor touchscreen beside cabled equipment"></div>
    <div class="hero-band"></div>
    <h1 class="hero-title"><span class="hero-title__small">MEDICAL DEVICE</span><span class="hero-title__large">CASE STUDY</span></h1>
    <div class="hero-rule"></div>

    <div class="section col-left" style="top:286px">
      <div class="section__head">
        <svg class="section__icon" viewBox="0 0 22 22"><circle cx="11" cy="11" r="10" fill="none" stroke="#13275a" stroke-width="1.2"/><path d="M11 5.5a3 3 0 0 1 3 3c0 2.2-3 5.5-3 5.5s-3-3.3-3-5.5a3 3 0 0 1 3-3z" fill="none" stroke="#6f8fb4" stroke-width="1"/><path d="M7 16h8" stroke="#6f8fb4" stroke-width="1"/></svg>
        <h2 class="section__title">SITUATION</h2>
      </div>
      <div class="section__body" style="height:174px">
        <p>This section introduces the client and sets the scene for the case study. Describe the facility, its size and the team involved, along with the clinical areas that rely on the equipment every day. Explain how devices were sourced, serviced and tracked before the project began, and note any pressure from patient volume, budget limits or upcoming audits. Mention the people who first reached out and what they hoped to gain from working with a trusted partner. Keep the tone warm and factual, and use plain words that a busy clinical manager can scan in a minute. A short quote from a nurse, technician or director adds a personal voice and helps the reader picture the setting before the story moves on to the details that shaped the project from its very first week.</p>
        <p>Close the situation with a clear summary of where things stood. List the main devices in use, the age of the fleet and any gaps in service records. Note how many staff used each device and how often repairs pulled units out of service. This gives context for the challenge that follows and shows that the team took time to understand the site before proposing a single change to equipment or workflow, which readers value highly.</p>
      </div>
    </div>

    <div class="section col-left" style="top:493px">
      <div class="section__head">
        <svg class="section__icon" viewBox="0 0 22 22"><circle cx="11" cy="11" r="10" fill="none" stroke="#13275a" stroke-width="1.2"/><path d="M6.5 15l3.5-4 2.5 2.5 3.5-5" fill="none" stroke="#6f8fb4" stroke-width="1.2"/><path d="M13.5 8.5h2.5v2.5" fill="none" stroke="#6f8fb4" stroke-width="1.2"/></svg>
        <h2 class="section__title">CHALLENGE</h2>
      </div>
      <div class="section__body" style="height:72px">
        <p>Describe the core problem in a few direct sentences. Was equipment failing too often, were service costs rising, or did staff lack training on new devices? Show the impact on patients, schedules and budgets with one or two simple figures. Explain why earlier attempts did not solve the issue and what was at stake if nothing changed. Keep this section focused so the reader clearly sees the need before reading about the solution that was put in place.</p>
      </div>
    </div>

    <div class="section col-right" style="top:286px">
      <div class="section__head">
        <svg class="section__icon" viewBox="0 0 22 22"><circle cx="11" cy="11" r="10" fill="none" stroke="#13275a" stroke-width="1.2"/><path d="M7 11.5l2.6 2.6L15 8.5" fill="none" stroke="#6f8fb4" stroke-width="1.4"/></svg>
        <h2 class="section__title">SOLUTION</h2>
      </div>
      <div class="section__body" style="height:72px">
        <p>Outline the equipment and services that were delivered. Name the device types, the setup plan and the training given to staff on each shift. Highlight how the team stayed close to the client, answered questions quickly and adjusted the plan as needs became clearer. Note the timeline from first visit to full use, and any support that continues today.</p>
      </div>
    </div>

    <div class="section col-right" style="top:391px">
      <div class="section__head">
        <svg class="section__icon" viewBox="0 0 22 22"><circle cx="11" cy="11" r="10" fill="none" stroke="#13275a" stroke-width="1.2"/><path d="M7.5 15.5v-3M10.2 15.5v-5M12.9 15.5v-7M15.6 15.5v-4" stroke="#6f8fb4" stroke-width="1.6"/></svg>
        <h2 class="section__title">RESULTS</h2>
      </div>
      <div class="section__body" style="height:72px">
        <p>Share the measurable outcomes in plain numbers. Report changes in device uptime, repair costs, response times or staff confidence after the rollout. Where possible, compare the figures with the starting point described earlier. A short comment from the client helps turn the numbers into a story and shows the real value the partnership brought to patient care.</p>
      </div>
    </div>

    <div class="section col-right" style="top:493px">
      <div class="section__head">
        <svg class="section__icon" viewBox="0 0 22 22"><circle cx="11" cy="11" r="10" fill="none" stroke="#13275a" stroke-width="1.2"/><circle cx="11" cy="10" r="3.2" fill="none" stroke="#6f8fb4" stroke-width="1.1"/><path d="M9.6 14.5h2.8M11 4v1.3M5.5 10h1.3M15.2 10h1.3M7.2 6.2l.9.9M14.8 6.2l-.9.9" stroke="#6f8fb4" stroke-width="1"/></svg>
        <h2 class="section__title">CONCLUSION</h2>
      </div>
      <div class="section__body" style="height:72px">
        <p>Wrap up with the lasting benefit of the project and what comes next for the client. Restate the key result in one line, then look ahead to future plans, upgrades or new sites. End on a friendly note that reflects the personal service behind the work, and invite readers facing similar needs to get in touch for a conversation.</p>
      </div>
    </div>

    <div class="footer-rule"></div>
    <svg class="footer-corner" width="30" height="44" viewBox="0 0 30 44"><polygon points="5,44 30,0 30,44" fill="#0c2559"/><polygon points="0,44 3,44 28,0 25,0" fill="#b9bcc4"/></svg>
    <footer class="footer">
      <span class="contact"><svg viewBox="0 0 16 16"><circle cx="8" cy="8" r="7" fill="none" stroke="#fff" stroke-width="1"/><path d="M5.5 4.8l1.3-.3.8 1.8-.9.7c.4 1 1.1 1.7 2.1 2.1l.7-.9 1.8.8-.3 1.3c-3 .3-5.8-2.5-5.5-5.5z" fill="#fff"/></svg>+10000 24680</span>
      <span class="contact-sep">|</span>
      <span class="contact"><svg viewBox="0 0 16 16"><circle cx="8" cy="8" r="7" fill="none" stroke="#fff" stroke-width="1"/><circle cx="8" cy="8" r="4" fill="none" stroke="#fff" stroke-width=".8"/><path d="M4 8h8M8 4c-1.6 2.4-1.6 5.6 0 8M8 4c1.6 2.4 1.6 5.6 0 8" fill="none" stroke="#fff" stroke-width=".8"/></svg>www.valtu.com</span>
      <span class="contact-sep">|</span>
      <span class="contact"><svg viewBox="0 0 16 16"><circle cx="8" cy="8" r="7" fill="none" stroke="#fff" stroke-width="1"/><rect x="4.5" y="5.5" width="7" height="5" fill="none" stroke="#fff" stroke-width=".9"/><path d="M4.5 5.5L8 8.5l3.5-3" fill="none" stroke="#fff" stroke-width=".9"/></svg>info@valtu.com</span>
    </footer>
  </section>

  <!-- BACK PAGE -->
  <section class="page page--back">
    <div class="text-block" style="left:25px;top:24px;width:212px">
      <h2 class="text-block__title">LOREM IPSUM</h2>
      <div class="text-block__body" style="height:230px">
        <p>Use this page to go deeper into the project. Walk through the key steps in order, from the first site visit and needs review to device selection, delivery and installation. Explain the choices that were made and why they suited this client best. Short paragraphs keep the page easy to read, and subheads can be renamed to match the story being told in each new case study. Where it helps, note the dates of each stage, the people involved on both sides and any changes made along the way so the reader can follow the project from start to finish without effort.</p>
        <p>Add detail on training and support. Describe how staff were shown each device, how questions were handled during the first weeks and how service visits were planned. Include any checklists, reports or online tools that made the work smoother for the clinical team. Mention the named contact who looked after the account, since readers value knowing a real person will be there when they call. This builds trust and shows the care behind every delivery. A brief note on spare parts, loan units and after-hours cover can also reassure readers who worry about downtime on busy wards.</p>
        <p>Finish this column with a brief note on lessons learned. What would the team repeat on the next project, and what did the client say made the biggest difference to their daily work? One honest sentence about what was improved along the way makes the story feel real and shows a team that keeps learning.</p>
      </div>
    </div>

    <div class="photo photo--monitor" role="img" aria-label="Benchtop patient vital signs monitor on a stand"></div>

    <div class="text-block" style="left:258px;top:211px;width:200px">
      <h2 class="text-block__title">ABOUT VALTU</h2>
      <div class="text-block__body" style="height:34px;margin-top:8px">
        <p>Valtu supplies and services medical equipment for clinics, labs and hospitals. Our team pairs deep device knowledge with friendly, personal support, so every client has a trusted partner from first call to long after setup.</p>
      </div>
    </div>

    <div class="photo photo--clinician" role="img" aria-label="Clinician in scrubs and cap operating bedside monitoring equipment"></div>

    <div class="text-block" style="left:256px;top:291px;width:226px">
      <h2 class="text-block__title">LOREM IPSUM</h2>
      <div class="text-block__body" style="height:275px">
        <p>Use this column for supporting facts. A short list of devices supplied, the number of units installed and the departments served helps readers judge whether the project matches their own needs. You can also note certifications held, service hours offered and the average response time for repairs. Keep figures current and check them with the client before the case study is shared. If space allows, add a line on how devices were tested before use and how records are kept for future audits.</p>
        <p>A second paragraph can expand on the client relationship. Describe regular check-ins, planned maintenance and how feedback from staff shaped later updates. Readers want to see a partner who listens, adapts and stays involved after the sale, so give one clear example of this in action. A named quote from a ward manager or lab lead works well here, as it puts a real voice behind the claims and shows that the support continues long after installation day.</p>
        <p>Use the final paragraph for a call to action. Invite readers to email the team for more details, a product demo or a copy of the full project report. Mention that every enquiry gets a personal reply from a specialist who knows the equipment well and understands clinical needs. Point to the contact details below so the next step is easy and clear for every reader.</p>
        <p>Email us today to start a conversation about your own equipment needs and goals. Our team is ready to help you plan the next step with care.</p>
      </div>
    </div>

    <div class="footer-rule"></div>
    <svg class="footer-corner" width="30" height="44" viewBox="0 0 30 44"><polygon points="5,44 30,0 30,44" fill="#0c2559"/><polygon points="0,44 3,44 28,0 25,0" fill="#b9bcc4"/></svg>
    <footer class="footer">
      <span class="contact"><svg viewBox="0 0 16 16"><circle cx="8" cy="8" r="7" fill="none" stroke="#fff" stroke-width="1"/><path d="M5.5 4.8l1.3-.3.8 1.8-.9.7c.4 1 1.1 1.7 2.1 2.1l.7-.9 1.8.8-.3 1.3c-3 .3-5.8-2.5-5.5-5.5z" fill="#fff"/></svg>+10000 24680</span>
      <span class="contact-sep">|</span>
      <span class="contact"><svg viewBox="0 0 16 16"><circle cx="8" cy="8" r="7" fill="none" stroke="#fff" stroke-width="1"/><circle cx="8" cy="8" r="4" fill="none" stroke="#fff" stroke-width=".8"/><path d="M4 8h8M8 4c-1.6 2.4-1.6 5.6 0 8M8 4c1.6 2.4 1.6 5.6 0 8" fill="none" stroke="#fff" stroke-width=".8"/></svg>www.valtu.com</span>
      <span class="contact-sep">|</span>
      <span class="contact"><svg viewBox="0 0 16 16"><circle cx="8" cy="8" r="7" fill="none" stroke="#fff" stroke-width="1"/><rect x="4.5" y="5.5" width="7" height="5" fill="none" stroke="#fff" stroke-width=".9"/><path d="M4.5 5.5L8 8.5l3.5-3" fill="none" stroke="#fff" stroke-width=".9"/></svg>info@valtu.com</span>
    </footer>
  </section>

</div>
</body>
</html>
```